Brell Harbor Company Business Cards

Front and Back Business Card - logo and text setup - cool design. I need workable photoshop or illustrator files so I can setup each employee card with design that is created
Updates

Hi everyone, thank you for the great entries. Please no more white and blue cards - there are so many already - black and silver only now please. thanks!

Target Market(s)

Construction Industry - Facility Managers

Industry/Entity Type

Construction

Contact Information for Business Card

I really like contemporary simplistic looks - clean neat....not opposed to seeing some black backrounds

Requirements
Must have
• Logo/website address with design on front only - www.brellharbor-example.com (logo attached)
• Back:
• Name/Title/Company Address/Phone/email address
Nice to have
• Cool design
Should not have
• Nothing gimmicky like Fire or Water - since we are a Fire Protection company - it has all been done

```html
<!DOCTYPE html>
<html lang="en">
<head>
<meta charset="utf-8">
<title>Brell Harbor Company – Business Card</title>
<link rel="stylesheet" href="https://fonts.googleapis.com/css2?family=Tinos:wght@400;700&display=swap">
<style>
  :root {
    --card-black: #1b1b1e;
    --card-charcoal: #2a2a2f;
    --silver: #c6c9ce;
    --silver-light: #e6e8eb;
    --silver-dim: #8d9096;
    --paper: #ffffff;
  }
  * { margin: 0; padding: 0; box-sizing: border-box; }
  html, body {
    width: 1007px;
    height: 1200px;
    overflow: hidden;
    background: var(--paper);
  }
  .sheet { position: relative; width: 1007px; height: 1200px; }

  /* Front */
  .card-front {
    position: absolute;
    left: 2px; top: 0;
    width: 1003px; height: 602px;
    background: var(--card-black);
  }
  .brand-lockup {
    position: absolute;
    left: 0; right: 0; top: 250px;
    display: flex;
    align-items: center;
    justify-content: center;
    gap: 20px;
  }
  .brand-mark {
    width: 44px; height: 44px;
    background: var(--silver);
  }
  .brand-name {
    font-family: "Tinos", "Times New Roman", serif;
    font-weight: 700;
    font-size: 66px;
    line-height: 1;
    color: var(--silver);
    white-space: nowrap;
  }
  .brand-rule {
    position: absolute;
    left: 150px; right: 150px; top: 355px;
    height: 2px;
    background: linear-gradient(90deg, transparent, var(--silver-dim), transparent);
  }
  .front-web {
    position: absolute;
    left: 0; right: 0; top: 378px;
    text-align: center;
    font-family: "Tinos", "Times New Roman", serif;
    font-size: 22px;
    letter-spacing: 2px;
    color: var(--silver-light);
  }

  /* Back */
  .card-back {
    position: absolute;
    left: 0; top: 612px;
    width: 1007px; height: 588px;
    background: var(--card-black);
    overflow: hidden;
  }
  .back-pattern {
    position: absolute;
    left: 185px; top: 0;
    width: 822px; height: 588px;
    background:
      radial-gradient(ellipse at 25% 20%, rgba(198,201,206,0.22), rgba(198,201,206,0.04) 65%),
      var(--card-charcoal);
  }
  .contact {
    position: absolute;
    left: 240px; top: 0; right: 0; bottom: 0;
    font-family: "Tinos", "Times New Roman", serif;
    color: var(--silver-light);
  }
  .contact-name {
    position: absolute;
    top: 100px;
    font-weight: 400;
    font-size: 52px;
    line-height: 1;
    white-space: nowrap;
  }
  .contact-title {
    position: absolute;
    top: 162px;
    font-size: 19px;
    letter-spacing: 2px;
    color: var(--silver);
    white-space: nowrap;
  }
  .contact-line {
    position: absolute;
    white-space: nowrap;
    letter-spacing: 1.5px;
    line-height: 1;
  }
  .contact-address { top: 222px; font-size: 20px; }
  .contact-phone { top: 300px; font-size: 19px; }
  .contact-phone .number { font-size: 28px; margin-left: 10px; }
  .contact-phone-alt { top: 378px; left: 81px; font-size: 28px; }
  .contact-web { top: 456px; font-size: 20px; }
</style>
</head>
<body>
<main class="sheet">
  <section class="card-front">
    <div class="brand-lockup">
      <span class="brand-mark" aria-hidden="true"></span>
      <span class="brand-name">Brell Harbor Company</span>
    </div>
    <div class="brand-rule" aria-hidden="true"></div>
    <p class="front-web">www.brellharbor-example.com</p>
  </section>

  <section class="card-back">
    <div class="back-pattern" role="img" aria-label="Repeating brush-stroke pattern in silver tones"></div>
    <div class="contact">
      <h1 class="contact-name">Dana Whitfield</h1>
      <p class="contact-title">Project Manager · Brell Harbor Company</p>
      <p class="contact-line contact-address">ADDRESS / 48 Quarry Lane Millbrook, NY 12545</p>
      <p class="contact-line contact-phone">Phone <span class="number">(555) 014-2260</span></p>
      <p class="contact-line contact-phone-alt">(555) 014-2263</p>
      <p class="contact-line contact-web">info@brellharbor-example.com &nbsp;/&nbsp; www.brellharbor-example.com</p>
    </div>
  </section>
</main>
</body>
</html>
```